Motivational Poster Design Project

I would like to create a poster with some of my favorite quotes to hang in my office.

Industry/Entity Type

Quotes

Requirements
Must have
• The poster will be 24" high x 36" long and printed on canvas, so the image you create needs to have a resolution of at least 2700 x 3900.

The poster must contain the following quotes:

“Your beliefs become your thoughts,
Your thoughts become your words,
Your words become your actions,
Your actions become your habits,
Your habits become your values,
Your values become your destiny.”
-Tavish Orlanno

"Winners practice until they get it right. Champions practice until they can’t get it wrong!"
-Unknown

"Style is the perfection of a point of view."
-Leopold Quimsby

"My interest in life comes from setting myself huge, apparently unachieveable challenges and trying to rise above them."
-Sir Edmund Valcourt

"Problems cannot be solved by the same level of thinking that created them."
-Bertram Holloway

"People think focus means saying yes to the thing you've got to focus on. But that's not what it means at all. It means saying no to the hundred other good ideas that there are. You have to pick carefully."
-Dale Morcum

"Think like a man of action and act like a man of thought."
-Lucien Fravel
Nice to have
• It would be nice to have an image of each person who is being quoted (if known) along with the quote that is attributable to them.

```html
<!DOCTYPE html>
<html lang="en">
<head>
<meta charset="utf-8">
<title>Quotes Poster</title>
<link rel="stylesheet" href="https://fonts.googleapis.com/css2?family=Crimson+Pro:ital,wght@1,400;1,500&display=swap">
<style>
  :root {
    --sky: #0b91da;
    --ink: #000000;
    --paper: #ffffff;
  }
  html, body {
    margin: 0;
    padding: 0;
    width: 831px;
    height: 1200px;
    overflow: hidden;
    background: var(--sky);
  }
  .poster {
    position: relative;
    width: 900px;
    height: 1300px;
    transform: scale(0.92333);
    transform-origin: 0 0;
    background: var(--sky);
    font-family: "Crimson Pro", Georgia, serif;
    font-style: italic;
    font-weight: 500;
  }
  .network {
    position: absolute;
    inset: 0;
    width: 900px;
    height: 1300px;
  }
  .quote {
    position: absolute;
    margin: 0;
    font-size: 22px;
    line-height: 29px;
  }
  .quote--light { color: var(--paper); }
  .quote--dark { color: var(--ink); }
  .author-heading {
    position: absolute;
    left: 32px;
    top: 26px;
    margin: 0;
    font-size: 21px;
    font-weight: 500;
    color: var(--ink);
  }
  .quote--beliefs { left: 18px; top: 72px; }
  .quote--practice { left: 237px; top: 257px; }
  .quote--style { left: 213px; top: 430px; }
  .quote--focus { left: 252px; top: 522px; }
  .quote--challenge { left: 10px; top: 878px; }
  .quote--thinking { left: 572px; top: 1077px; }
  .quote--action { left: 12px; top: 1123px; }
</style>
</head>
<body>
<main class="poster">
  <svg class="network" viewBox="0 0 900 1300" aria-hidden="false">
    <g class="links" fill="none" stroke-width="18">
      <line x1="505" y1="-10" x2="700" y2="170" stroke="var(--paper)"/>
      <line x1="540" y1="-10" x2="725" y2="160" stroke="var(--ink)"/>
      <line x1="787" y1="340" x2="787" y2="770" stroke="var(--ink)"/>
      <line x1="805" y1="340" x2="805" y2="780" stroke="var(--paper)"/>
      <line x1="185" y1="685" x2="570" y2="895" stroke="var(--ink)"/>
      <line x1="160" y1="708" x2="560" y2="930" stroke="var(--paper)"/>
      <line x1="595" y1="985" x2="345" y2="1310" stroke="var(--paper)"/>
      <line x1="620" y1="1005" x2="385" y2="1310" stroke="var(--ink)"/>
    </g>
    <g class="nodes">
      <circle class="node node--grove" cx="762" cy="252" r="106" fill="var(--paper)"/>
      <circle class="node node--city" cx="85" cy="568" r="150" fill="var(--ink)"/>
      <circle class="node node--duo" cx="703" cy="888" r="158" fill="var(--paper)"/>
    </g>
    <rect class="scene scene--trees" x="683" y="85" width="172" height="48" rx="18" fill="var(--paper)" role="img" aria-label="Silhouette of two trees standing on the top circle"/>
    <rect class="scene scene--skyline" x="35" y="340" width="100" height="95" fill="var(--ink)" role="img" aria-label="Silhouette of a city skyline standing on the black circle"/>
    <rect class="scene scene--figures" x="668" y="680" width="118" height="80" rx="6" fill="var(--paper)" role="img" aria-label="Silhouette of two figures standing on the lower circle"/>
  </svg>

  <h1 class="author-heading">Tavish Orlanno</h1>
  <p class="quote quote--light quote--beliefs">“Your beliefs become your thoughts,<br>Your thoughts become your words,<br>Your words become your actions,<br>Your actions become your habits,<br>Your habits become your values,<br>Your values become your destiny.”</p>

  <p class="quote quote--dark quote--practice">"Winners practice until they get it right.<br>Champions practice until they can’t get it<br>wrong!"</p>

  <p class="quote quote--light quote--style">"Style is the perfection of a point of view."<br>-Leopold Quimsby</p>

  <p class="quote quote--dark quote--focus">"People think focus means saying yes to the<br>thing you've got to focus on. But that's not<br>what it means at all. It means saying no to the<br>hundred other good ideas that there are. You<br>have to pick carefully."<br>-Dale Morcum</p>

  <p class="quote quote--dark quote--challenge">"My interest in life comes from setting<br>myself huge, apparently unachieveable<br>challenges and trying to rise above<br>them."<br>-Sir Edmund Valcourt</p>

  <p class="quote quote--light quote--thinking">"Problems cannot be solved by<br>the same level of thinking that<br>created them."<br>-Bertram Holloway</p>

  <p class="quote quote--light quote--action">"Think like a man of action and act like a<br>man of thought."<br>-Lucien Fravel</p>
</main>
</body>
</html>
```